CD-Cover Desig für neues Album eines Liedermacher-Duos
Zielgruppe
Wir sind ein Liedermacher-Duo und benötigen für unser neues Album mit dem Titel 'Kiesel' ein Cover.
Infos über den Themenbereich der Songs findet man hier: https://www.vorhabenwerk.de/cd-kiesel
Aufgabenstellung
Cover könnte schlicht sein... oder auch kreativ verspielt mit warmen Farben und Formen... aber nicht kitschig.
'Kiesel' im Sinne von Geborgenheit also kein verzehrendes Feuer.. eher sonnig.
Evtl. könnte man unsere beiden Hauptinstrumente (Geige und Gitarre) andeuten.
Sonst stehen auf dem Cover nur noch unsere Namen: Dorothea Lindner & Jörg Haberl

```html
<!DOCTYPE html>
<html lang="de">
<head>
<meta charset="utf-8">
<title>Kiesel – Albumcover</title>
<link rel="stylesheet" href="https://fonts.googleapis.com/css2?family=Poiret+One&family=Arimo:wght@400&display=swap">
<style>
  :root {
    --page: #ffffff;
    --ink: #5b4a44;
    --peach-light: #f7dccb;
    --peach: #eeb892;
    --apricot: #e49a62;
    --amber: #e8a43a;
    --orange: #d9772e;
    --olive: #9a8a3a;
    --bark: #5a3e22;
  }
  html, body {
    margin: 0;
    padding: 0;
    width: 1200px;
    height: 1200px;
    overflow: hidden;
    background: var(--page);
  }
  .canvas {
    position: relative;
    width: 1200px;
    height: 1200px;
    background: var(--page);
  }
  .cover {
    position: absolute;
    left: 244px;
    top: 262px;
    width: 713px;
    height: 714px;
    overflow: hidden;
  }
  .cover-artwork {
    position: absolute;
    inset: 0;
    width: 100%;
    height: 100%;
  }
  .album-title {
    position: absolute;
    left: 30px;
    top: 96px;
    margin: 0;
    font-family: "Poiret One", sans-serif;
    font-weight: 400;
    font-size: 100px;
    line-height: 1;
    letter-spacing: 4px;
    color: var(--ink);
    -webkit-text-stroke: 1.6px var(--ink);
  }
  .album-artists {
    position: absolute;
    left: 33px;
    top: 218px;
    margin: 0;
    font-family: "Arimo", Arial, sans-serif;
    font-size: 18.5px;
    font-weight: 400;
    color: var(--ink);
    letter-spacing: 0.1px;
  }
</style>
</head>
<body>
<main class="canvas">
  <section class="cover">
    <svg class="cover-artwork" viewBox="0 0 713 714" preserveAspectRatio="none" role="img"
         aria-label="Gemalte Abendlandschaft in Pfirsich- und Orangetönen: See mit bewaldeter Insel, zwei Vögel am Himmel, rechts ein Baum mit gelbem und braunem Laub">
      <defs>
        <linearGradient id="sky" x1="0" y1="0" x2="0" y2="1">
          <stop offset="0" stop-color="var(--apricot)"/>
          <stop offset="0.3" stop-color="var(--peach-light)"/>
          <stop offset="0.7" stop-color="var(--peach-light)"/>
          <stop offset="1" stop-color="var(--peach)"/>
        </linearGradient>
        <radialGradient id="glow" cx="0.82" cy="0.45" r="0.55">
          <stop offset="0" stop-color="#f3d24a" stop-opacity="0.9"/>
          <stop offset="0.5" stop-color="var(--amber)" stop-opacity="0.55"/>
          <stop offset="1" stop-color="var(--amber)" stop-opacity="0"/>
        </radialGradient>
        <radialGradient id="canopy" cx="0.78" cy="0.55" r="0.45">
          <stop offset="0" stop-color="var(--olive)" stop-opacity="0.55"/>
          <stop offset="0.7" stop-color="var(--bark)" stop-opacity="0.25"/>
          <stop offset="1" stop-color="var(--bark)" stop-opacity="0"/>
        </radialGradient>
        <radialGradient id="corner" cx="1" cy="0" r="0.5">
          <stop offset="0" stop-color="var(--orange)" stop-opacity="0.85"/>
          <stop offset="1" stop-color="var(--orange)" stop-opacity="0"/>
        </radialGradient>
      </defs>
      <rect width="713" height="714" fill="url(#sky)"/>
      <rect width="713" height="714" fill="url(#corner)"/>
      <rect width="713" height="714" fill="url(#glow)"/>
      <rect width="713" height="714" fill="url(#canopy)"/>
    </svg>
    <h1 class="album-title">KIESEL</h1>
    <p class="album-artists">Dorothea Lindner &amp; Jörg Haberl</p>
  </section>
</main>
</body>
</html>
```